Dermatology Office Business Card Update

Updating some information on the current business card. Do not adjust font type. Need both rounded rectangle and rounded square card files. In addition, must have separate file for both rectangle and square cards for gold foil printing.1. Update phone number with: 555-318-27602. Remove email address3. Add this website to be listed under quillbrookdermatology.example:jilluxe.com4. Under updated phone number, add the flickvue logo in color and then a space and the following text: @dermjill5. Gold foil should be inclusive of the outline of the butterfly wings on the front. Also should put a small hyphen that is also gold foil under the cursive Nora Belcastro, MD and before the block lettering begins.Back of card remains the samePlease feel free to contact me with any questions!

Target Market(s)

Patients

Contact Information for Business Card

Just needs some updates along with files for gold foil printing

Requirements
Must have
• Updating some information on the current business card. Do not adjust font type. Need both rounded rectangle and rounded square card files. In addition, must have separate file for both rectangle and square cards for gold foil printing.
• 1. Update phone number with: 555-318-2760
• 2. Remove email address
• 3. Add this website to be listed under quillbrookdermatology.example:
• norvatek.example
• 4. Under updated phone number, add the flickvue logo in color and then a space and the following text: @docnorabel
• 5. Gold foil should be inclusive of the outline of the butterfly wings on the front. Also should put a small hyphen that is also gold foil under the cursive Nora Belcastro, MD and before the block lettering begins.
• Back of card remains the same
• Please feel free to contact me with any questions!

```html
<!DOCTYPE html>
<html lang="en">
<head>
<meta charset="utf-8">
<title>Quillbrook Dermatology – Business Card</title>
<link rel="stylesheet" href="https://fonts.googleapis.com/css2?family=Josefin+Sans:wght@400;600&family=Quicksand:wght@500&display=swap">
<style>
  :root {
    --navy: #2b3654;
    --mauve: #b98a92;
    --gold: #c9a24a;
    --paper: #ffffff;
    --stage: #fdfdfd;
    --edge: #c8c8c8;
    --wash-rose: #c39aa0;
    --wash-plum: #9c6e7a;
    --wash-lilac: #86718a;
    --wash-navy: #3d4e7a;
  }
  * { box-sizing: border-box; margin: 0; padding: 0; }
  html, body {
    width: 1200px; height: 1200px; overflow: hidden;
    background: var(--stage);
  }
  .canvas { position: relative; width: 1200px; height: 1200px; }

  .card {
    position: absolute; left: 284px; width: 632px; height: 362px;
    border-radius: 37px; overflow: hidden;
    border: 1px solid var(--edge);
  }
  .card--front { top: 229px; background: var(--paper); }
  .card--back {
    top: 609px;
    background:
      radial-gradient(ellipse at 15% 20%, rgba(214,176,180,.7), transparent 55%),
      radial-gradient(ellipse at 95% 95%, var(--wash-navy), transparent 45%),
      linear-gradient(110deg, var(--wash-rose) 0%, var(--wash-plum) 40%, var(--wash-lilac) 75%, var(--wash-navy) 100%);
  }

  .centered { position: absolute; left: 0; right: 0; text-align: center; }

  .brand-dot {
    position: absolute; left: 296px; top: 48px;
    width: 40px; height: 40px; border-radius: 50%;
    background: var(--mauve);
  }
  .brand-name {
    top: 112px;
    font-family: "Josefin Sans", sans-serif; font-weight: 600;
    font-size: 18px; line-height: 21px; letter-spacing: 3.4px;
    color: var(--navy);
  }
  .brand-byline {
    top: 156px;
    font-family: "Josefin Sans", sans-serif; font-weight: 400;
    font-size: 11px; letter-spacing: 2.4px;
    color: var(--mauve);
  }
  .gold-dash {
    position: absolute; left: 309px; top: 180px;
    width: 14px; height: 2px; background: var(--gold);
  }
  .doctor-name {
    top: 193px;
    font-family: "Josefin Sans", sans-serif; font-weight: 400;
    font-size: 20px; letter-spacing: 2.8px; color: var(--navy);
  }
  .doctor-name .credential { color: var(--mauve); }
  .doctor-name .rule {
    display: inline-block; width: 2px; height: 22px;
    background: var(--gold); vertical-align: -3px; margin: 0 10px;
  }
  .phone {
    top: 228px;
    font-family: "Josefin Sans", sans-serif; font-weight: 600;
    font-size: 21px; letter-spacing: 2.8px; color: var(--navy);
  }
  .social {
    top: 255px;
    font-family: "Quicksand", sans-serif; font-weight: 500;
    font-size: 17px; color: var(--navy);
  }
  .social .mark {
    display: inline-block; width: 18px; height: 18px;
    background: var(--navy); border-radius: 4px;
    vertical-align: -3px; margin-right: 8px;
  }
  .social .handle { margin-left: 10px; }

  .websites {
    position: absolute; left: 38px; top: 286px;
    list-style: none;
    font-family: "Quicksand", sans-serif; font-weight: 500;
    font-size: 20px; line-height: 24px; letter-spacing: .7px;
    color: var(--mauve);
  }
  .websites li::before {
    content: ""; display: inline-block;
    width: 5px; height: 5px; border-radius: 50%;
    background: var(--mauve); margin-right: 14px; vertical-align: 4px;
  }
  .wash-band {
    position: absolute; left: 0; right: 0; bottom: 0; height: 23px;
    background: linear-gradient(90deg, var(--wash-navy) 0%, var(--wash-lilac) 35%, var(--wash-plum) 75%, #a06e72 100%);
  }

  .back-dot {
    position: absolute; left: 296px; top: 100px;
    width: 40px; height: 40px; border-radius: 50%;
    background: var(--paper);
  }
  .back-brand {
    top: 154px;
    font-family: "Josefin Sans", sans-serif; font-weight: 600;
    font-size: 26px; line-height: 30px; letter-spacing: 4px;
    color: var(--paper);
  }
  .tagline {
    top: 241px;
    font-family: "Josefin Sans", sans-serif; font-weight: 400;
    font-size: 15px; letter-spacing: 3.4px; color: var(--paper);
  }
</style>
</head>
<body>
<main class="canvas">

  <section class="card card--front" aria-label="Card front">
    <span class="brand-dot" aria-hidden="true"></span>
    <p class="centered brand-name">QUILLBROOK<br>DERMATOLOGY</p>
    <p class="centered brand-byline">BY NORA BELCASTRO MD</p>
    <span class="gold-dash" aria-hidden="true"></span>
    <p class="centered doctor-name"><span class="rule"></span>NORA BELCASTRO, <span class="credential">MD</span><span class="rule"></span></p>
    <p class="centered phone">555.318.2760</p>
    <p class="centered social"><span class="mark" aria-hidden="true"></span>flickvue<span class="handle">@docnorabel</span></p>
    <ul class="websites">
      <li>quillbrookdermatology.example</li>
      <li>norvatek.example</li>
    </ul>
    <div class="wash-band" role="img" aria-label="Watercolour wash band in navy and mauve"></div>
  </section>

  <section class="card card--back" role="img" aria-label="Card back: mauve to navy watercolour wash with brand name and tagline">
    <span class="back-dot" aria-hidden="true"></span>
    <p class="centered back-brand">QUILLBROOK</p>
    <p class="centered tagline">SKIN IN BLOOM</p>
  </section>

</main>
</body>
</html>
```